Business card design for Automotive workshop

We need a business card for a new automotive repair and tyre shop called Ridgeback Prime Automotive located in New Zealand. We are a clean, modern and fresh workshop and company.

Front needs to feature logo,
my name:
Lachie Westergaard (director)

Address:
48 Marlow Lane
Kerrowby 3582

Phone: 07 842 1937
Mobile: 027 519 2764
Email: office@ridgebackmotors.co.nz
Website: ridgebackmotors.co.nz

Back needs to feature an area to write down appointment details, date and time.

Also feature a list of jobs and work we do such as,
Vehicle Servicing
All Mechanical Repairs
Warrant of Fitness
Tyres & Wheel Alignments
Automotive Diagnostics
Automotive Parts & Supplies

```html
<!DOCTYPE html>
<html lang="en">
<head>
<meta charset="utf-8">
<title>Ridgeback Prime Automotive – Business Card</title>
<link rel="stylesheet" href="https://fonts.googleapis.com/css2?family=Roboto:wght@400;700&family=Roboto+Condensed:wght@400;700&family=Open+Sans:wght@600&display=swap">
<style>
  :root {
    --canvas: #f1f1f3;
    --card-dark: #161617;
    --card-dark-soft: #2c2c2e;
    --ring-dark: #1c1c1e;
    --ring-soft: #3a3a3d;
    --brand-red: #c41e3a;
    --ink-white: #ffffff;
    --ink-black: #111111;
    --stitch: rgba(255,255,255,0.85);
  }
  * { margin: 0; padding: 0; box-sizing: border-box; }
  html, body { width: 1200px; height: 1000px; overflow: hidden; }
  body { background: var(--canvas); position: relative; font-family: "Roboto", Arial, sans-serif; }

  .card { position: absolute; width: 510px; height: 510px; border-radius: 50%; }
  .card svg.card-art { position: absolute; inset: 0; width: 510px; height: 510px; }
  .card-front { left: 196px; top: 62px; }
  .card-back { left: 494px; top: 416px; }

  .holder-name { font-family: "Roboto Condensed", Arial, sans-serif; font-weight: 700; font-size: 24px; fill: var(--brand-red); }
  .holder-role { font-family: "Roboto", Arial, sans-serif; font-size: 14px; letter-spacing: 0.5px; fill: var(--ink-white); }

  .brand-name {
    position: absolute; left: 0; right: 0; top: 188px; text-align: center;
    font-family: "Roboto Condensed", Arial, sans-serif; font-weight: 700;
    font-size: 25px; letter-spacing: 1px; color: var(--brand-red); text-transform: uppercase;
  }

  .contact-list { position: absolute; left: 106px; top: 272px; list-style: none; color: var(--ink-white); font-size: 17.5px; }
  .contact-item { display: flex; align-items: center; height: 31px; }
  .contact-icon { width: 18px; height: 18px; margin-right: 12px; flex: none; }
  .contact-gap { width: 26px; }

  .service-ring { font-family: "Open Sans", Arial, sans-serif; font-weight: 600; font-size: 15.5px; fill: var(--ink-white); }

  .appointment { position: absolute; left: 74px; top: 192px; width: 376px; font-family: "Roboto", Arial, sans-serif; font-weight: 700; font-size: 17px; color: var(--ink-black); }
  .appointment-row { display: flex; align-items: flex-end; height: 42px; }
  .appointment-label { flex: none; margin-right: 6px; }
  .appointment-line { flex: 1; border-bottom: 2.5px dotted var(--ink-black); margin-bottom: 5px; }
</style>
</head>
<body>

<section class="card card-front">
  <svg class="card-art" viewBox="0 0 510 510">
    <defs>
      <radialGradient id="front-tread" cx="50%" cy="45%" r="55%">
        <stop offset="0%" stop-color="var(--card-dark-soft)"/>
        <stop offset="100%" stop-color="var(--card-dark)"/>
      </radialGradient>
      <path id="name-arc" d="M 160 128 Q 255 84 350 128"/>
    </defs>
    <circle cx="255" cy="255" r="255" fill="url(#front-tread)" role="img" aria-label="Dark tyre tread texture"/>
    <circle cx="255" cy="255" r="236" fill="none" stroke="var(--stitch)" stroke-width="1" stroke-dasharray="5 4"/>
    <circle cx="255" cy="255" r="221" fill="none" stroke="var(--stitch)" stroke-width="1" stroke-dasharray="5 4"/>
    <text class="holder-name"><textPath href="#name-arc" startOffset="50%" text-anchor="middle">Lachie Westergaard</textPath></text>
    <text class="holder-role" x="255" y="128" text-anchor="middle">DIRECTOR</text>
  </svg>

  <div class="brand-name">Ridgeback Prime Automotive</div>

  <ul class="contact-list">
    <li class="contact-item">
      <svg class="contact-icon" viewBox="0 0 20 20" fill="none" stroke="var(--brand-red)" stroke-width="1.6"><path d="M10 18s-6-6.5-6-10.5a6 6 0 0 1 12 0C16 11.5 10 18 10 18z"/><circle cx="10" cy="7.5" r="2"/></svg>
      <span>48 Marlow Lane&nbsp;&nbsp;&nbsp;Kerrowby 3582</span>
    </li>
    <li class="contact-item">
      <svg class="contact-icon" viewBox="0 0 20 20" fill="var(--brand-red)"><path d="M4.5 2.5l3 .3 1.3 3.6-2 1.4a10 10 0 0 0 5.4 5.4l1.4-2 3.6 1.3.3 3a2 2 0 0 1-2.2 2A15 15 0 0 1 2.5 4.7a2 2 0 0 1 2-2.2z"/></svg>
      <span>07 842 1937</span>
      <span class="contact-gap"></span>
      <svg class="contact-icon" viewBox="0 0 20 20" fill="none" stroke="var(--brand-red)" stroke-width="1.5"><circle cx="10" cy="10" r="8"/><path d="M7 5.8l1.5.2.6 1.7-1 .7a5 5 0 0 0 2.6 2.6l.7-1 1.7.6.2 1.5a1 1 0 0 1-1.1 1A7 7 0 0 1 6 6.9a1 1 0 0 1 1-1.1z" fill="var(--brand-red)" stroke="none"/></svg>
      <span>027 519 2764</span>
    </li>
    <li class="contact-item">
      <svg class="contact-icon" viewBox="0 0 20 20" fill="none" stroke="var(--brand-red)" stroke-width="1.4"><circle cx="10" cy="10" r="8"/><ellipse cx="10" cy="10" rx="3.5" ry="8"/><path d="M2 10h16M3.5 6h13M3.5 14h13"/></svg>
      <span>ridgebackmotors.co.nz</span>
    </li>
    <li class="contact-item">
      <svg class="contact-icon" viewBox="0 0 20 20" fill="none" stroke="var(--brand-red)" stroke-width="1.5"><rect x="2" y="4.5" width="16" height="11"/><path d="M2 4.5l8 6.5 8-6.5M2 15.5l6-5.5M18 15.5l-6-5.5"/></svg>
      <span>office@ridgebackmotors.co.nz</span>
    </li>
  </ul>
</section>

<section class="card card-back">
  <svg class="card-art" viewBox="0 0 510 510">
    <defs>
      <radialGradient id="ring-tread" cx="50%" cy="50%" r="50%">
        <stop offset="78%" stop-color="var(--ring-soft)"/>
        <stop offset="100%" stop-color="var(--ring-dark)"/>
      </radialGradient>
      <path id="service-path" d="M 255 477 A 222 222 0 1 1 255 33 A 222 222 0 1 1 255 477"/>
    </defs>
    <circle cx="255" cy="255" r="255" fill="url(#ring-tread)" role="img" aria-label="Dark tyre tread ring"/>
    <circle cx="255" cy="255" r="204" fill="var(--ink-white)"/>
    <text class="service-ring"><textPath href="#service-path" startOffset="4" textLength="1385" lengthAdjust="spacing">-Vehicle Servicing - All Mechanical Repairs - Warrant of Fitness - Tyres &amp; Wheel Alignments - Automotive Diagnostics - Automotive Parts &amp; Supplies</textPath></text>
  </svg>

  <div class="appointment">
    <div class="appointment-row"><span class="appointment-label">Details:</span><span class="appointment-line"></span></div>
    <div class="appointment-row"><span class="appointment-label">Date:</span><span class="appointment-line"></span></div>
    <div class="appointment-row"><span class="appointment-label">Time:</span><span class="appointment-line"></span></div>
  </div>
</section>

</body>
</html>
```